Inspirational quote for home gym wall - Rashid Tenko quote

I'd like to design a poster for my home gym with a quote from Rashid Tenko

"The fight is won or lost far away from witnesses - behind the lines, in the gym, and out there on the road, long before I dance under those lights."

The size should be approximately 1.5 x 2 m.

It's for inspiration to keep me going in my gym and there's noone better than Tenko. I will get it printed onto canvas. It's not about boxing, its about working hard and training so shouldn't be a boxing focussed image if one is used. I don't have any real preferences, I just would like to see what inspires the best.

Font styles to use
Sans Serif

Colors
000000
ffffff
fbed33

Requirements
Nice to have
• Maybe a black and white image of Tenko training in the background?
• Some thoughts on type of images (doesn't have to be these ones)
• https://www.plorvistock.co.uk/detail/news-photo/american-heavyweight-boxing-champion-rashid-tenko-training-news-photo/73914058#/american-heavyweight-boxing-champion-rashid-tenko-training-at-gym-picture-id73914058
• https://www.zentrafind.co.uk/search?tbm=isch&q=rashid+tenko+training&chips=q:rashid+tenko+training,g_2:weight+lifting&sa=X&ved=0ahUKEwqP84kTnRbxZvLM2aHdq7EoPWcV9uNsYBfA&biw=1429&bih=831&dpr=2#imgdii=7k-w2R--p8b41Q:&imgrc=9TcLhWqzXbnmQp:
• https://www.zentrafind.co.uk/search?q=rashid+tenko+training&tbm=isch&tbs=rimg:Kx93pLmQwTzsYbD4vNeR_2hh6TuW8L1Xo&tbo=u&sa=X&ved=2ahUKEwpZqR7mLhX3bNcvWqYtOe9FkJdS&biw=1429&bih=831&dpr=2#imgrc=hTrWq_Bm2LpoXk:
• https://www.zentrafind.co.uk/search?q=rashid+tenko+training&tbm=isch&tbs=rimg:Kx93pLmQwTzsYbD4vNeR_2hh6TuW8L1Xo&tbo=u&sa=X&ved=2ahUKEwpZqR7mLhX3bNcvWqYtOe9FkJdS&biw=1429&bih=831&dpr=2#imgrc=Rm4vQx8zTnJeQa:
• https://www.zentrafind.co.uk/search?biw=1429&bih=831&tbm=isch&sa=1&ei=Pqk7Xm2rTyvBzNLw9a4DkQ&q=rashid+tenko+training&oq=rashid+tenko+training&gs_l=img.3...0.0.0.48261.0.0.0.0.0.0.0.0..0.0....0...1c..64.img..0.0.0....0.QvbT-K_otnE#imgrc=Lp7wQaxVgHzrNb:
• https://www.zentrafind.co.uk/search?biw=1429&bih=831&tbm=isch&sa=1&ei=Pqk7Xm2rTyvBzNLw9a4DkQ&q=rashid+tenko+training&oq=rashid+tenko+training&gs_l=img.3...0.0.0.48261.0.0.0.0.0.0.0.0..0.0....0...1c..64.img..0.0.0....0.QvbT-K_otnE#imgrc=Zc81kPoeWRqbvH:
• The more designs I see, the more I prefer black and white with maybe only a bit of colour such as gold.
Should not have
• I'm not a fan of red

```html
<!DOCTYPE html>
<html lang="en">
<head>
<meta charset="utf-8">
<title>The Fight – Rashid Tenko Quote Poster</title>
<link href="https://fonts.googleapis.com/css2?family=Bebas+Neue&display=swap" rel="stylesheet">
<style>
  :root {
    --paper: #ececec;
    --ink: #000000;
    --shade: #3a3a3a;
    --type: #ffffff;
  }
  html, body {
    margin: 0;
    padding: 0;
    width: 900px;
    height: 1200px;
    overflow: hidden;
    background: var(--paper);
  }
  .poster {
    position: relative;
    width: 900px;
    height: 1200px;
    overflow: hidden;
    background: var(--paper);
  }
  .poster__shapes {
    position: absolute;
    inset: 0;
    width: 900px;
    height: 1200px;
  }
  .poster__quote {
    position: absolute;
    left: 204px;
    top: 14px;
    margin: 0;
    font-family: "Bebas Neue", "Oswald", sans-serif;
    font-weight: 400;
    font-size: 84px;
    line-height: 67px;
    letter-spacing: 0.5px;
    color: var(--type);
    text-transform: uppercase;
    text-shadow: 0 0 2px rgba(0,0,0,0.55);
  }
  .poster__quote span {
    display: block;
    white-space: nowrap;
  }
</style>
</head>
<body>
  <main class="poster">
    <svg class="poster__shapes" viewBox="0 0 900 1200" xmlns="http://www.w3.org/2000/svg">
      <defs>
        <linearGradient id="photoTone" x1="0" y1="0" x2="1" y2="1">
          <stop offset="0" stop-color="#6a6a6a"/>
          <stop offset="0.45" stop-color="#2a2a2a"/>
          <stop offset="1" stop-color="#0b0b0b"/>
        </linearGradient>
      </defs>
      <!-- secondary grey band -->
      <polygon class="band band--shade" points="150,0 900,0 900,120 520,1200 260,1200" fill="var(--shade)"/>
      <!-- main black bolt -->
      <polygon class="band band--ink" points="210,0 900,0 900,300 470,1200 0,1200 0,420" fill="var(--ink)"/>
      <!-- training photograph area -->
      <rect class="poster__photo" x="0" y="480" width="600" height="720" fill="url(#photoTone)" opacity="0.85"
            role="img" aria-label="Black and white photograph of Rashid Tenko training, head bowed, shoulders in shadow"/>
    </svg>

    <h1 class="poster__quote" aria-label="The fight is won or lost far away from witnesses, behind the lines, in the gym, and out there on the road, long before I dance under those lights. — Rashid Tenko">
      <span>The fight</span>
      <span>is won or lost</span>
      <span>far away</span>
      <span>from witnesses</span>
      <span>behind the lines,</span>
      <span>in the gym,</span>
      <span>and out there</span>
      <span>on the road,</span>
      <span>long before</span>
      <span>I dance</span>
      <span>under those</span>
      <span>lights.</span>
    </h1>
  </main>
</body>
</html>
```